Kelvo Cube needs a packaging design

Hello!

I need an eye-catching package design for Kelvo Cube mobile accessories. The products inside the box package include a bluetooth speaker and a power bank.

This is under our brandname called Kelvo Cube. The text should be in the picture, no matter how the design looks.

I have attached pictures of the products. If you think that there will not be well with the images it is ok. Then these texts be included:
Bluetooth Speaker
Power Bank

This is our slogan:
Music + Power. It's your imagination that sets the limits!

The image will be printed on a carton pack containing with four color printing. Customising the picture for the type of print.

Should be in 300 DPI High resolution.

Please check the attached pictures where your design will be printed.
Also, I attached design inspiration images for reference. Feel free to do something similar like that.

For the size and dimensions please refer to this attachment:

So remember, the important thing is the design. Do your absolute best!

Reason: Hello everyone! I would like to see a design without the images of the accessories. Only text. I also dont want the text "Its you imagination that sets...". Thank you!

Target Market(s)

Mobile accessories

Industry/Entity Type

Electronics

Requirements
Must have
• This text:
• Kelvo Cube
Nice to have
• Music + Power.

```html
<!DOCTYPE html>
<html lang="en">
<head>
<meta charset="UTF-8">
<title>Kelvo Cube — Packaging Front Panel</title>
<link rel="stylesheet" href="https://fonts.googleapis.com/css2?family=Exo+2:wght@500;600;700&display=swap">
<style>
  :root {
    --stage-bg: #e9e8ec;
    --panel-deep: #0a0f3a;
    --panel-mid: #16238a;
    --panel-glow: #2a49d6;
    --title-cyan: #2fa6e6;
    --tagline-ink: #b9d4f2;
    --footnote-cyan: #3fb0e8;
    --band-shade: rgba(6, 10, 40, 0.45);
  }
  html, body {
    margin: 0;
    padding: 0;
    width: 1200px;
    height: 800px;
    overflow: hidden;
    background: var(--stage-bg);
  }
  .canvas {
    position: relative;
    width: 1200px;
    height: 800px;
    display: flex;
    align-items: center;
    justify-content: center;
  }
  .box-front {
    position: relative;
    width: 660px;
    height: 660px;
    background: var(--panel-deep);
    overflow: hidden;
    font-family: "Exo 2", sans-serif;
  }
  .circuit-artwork {
    position: absolute;
    inset: 0;
    background:
      radial-gradient(ellipse 55% 45% at 50% 45%, var(--panel-glow) 0%, rgba(42,73,214,0.35) 45%, transparent 75%),
      radial-gradient(ellipse 80% 70% at 50% 55%, var(--panel-mid) 0%, var(--panel-deep) 80%);
  }
  .title-band {
    position: absolute;
    left: 0;
    right: 0;
    top: 268px;
    height: 110px;
    background: var(--band-shade);
  }
  .brand-name {
    position: absolute;
    left: 0;
    right: 0;
    top: 268px;
    margin: 0;
    text-align: center;
    font-weight: 700;
    font-size: 72px;
    letter-spacing: 3px;
    color: var(--title-cyan);
    line-height: 1;
    text-transform: uppercase;
  }
  .tagline {
    position: absolute;
    left: 0;
    right: 0;
    top: 348px;
    margin: 0;
    text-align: center;
    font-weight: 600;
    font-size: 22px;
    letter-spacing: 1px;
    color: var(--tagline-ink);
  }
  .range-note {
    position: absolute;
    right: 30px;
    bottom: 26px;
    margin: 0;
    text-align: center;
    font-weight: 500;
    font-size: 17px;
    line-height: 1.2;
    letter-spacing: 1px;
    color: var(--footnote-cyan);
    text-transform: uppercase;
  }
</style>
</head>
<body>
  <main class="canvas">
    <section class="box-front">
      <div class="circuit-artwork" role="img" aria-label="Glowing blue circuit-board line pattern on a dark navy background"></div>
      <div class="title-band"></div>
      <h1 class="brand-name">Kelvo Cube</h1>
      <p class="tagline">Music + Power</p>
      <p class="range-note">All Mobile<br>Accesories</p>
    </section>
  </main>
</body>
</html>
```